Lantern Forge needs a business card

The logo we have uploaded is going to be the image centered on the back.
The business card color is going to be black. Increase the contrast in the logo and lettering so the grey stands out from the black and is more readable. Keep the shadow effect if you can.
On the front, the only part of the logo that should be used is the Egyptian character. We would like the following information included: Name (first last), Title, Phone number, email and company name (Lantern Forge).
The images of colored sound waves we uploaded is a concept we would like implemented on the front as well but please do not use the exact image. It is for guideline purposes.
Get creative with the empty space. We are a technology company that deals with sound and lights. Please not too busy.
Thank you, we look forward to all your submissions.

```html
<!DOCTYPE html>
<html lang="en">
<head>
<meta charset="UTF-8">
<title>Lantern Forge – Business Card</title>
<link href="https://fonts.googleapis.com/css2?family=Open+Sans:wght@400;600;700&display=swap" rel="stylesheet">
<style>
  :root {
    --backdrop: #2b2b2b;
    --card-black: #050505;
    --panel-grey: #6a6a6a;
    --text-dark: #000000;
    --brand-red: #e8363c;
    --rule: #111111;
    --wave-grey: #8a8a8a;
  }
  * { margin: 0; padding: 0; box-sizing: border-box; }
  html, body {
    width: 1200px; height: 900px; overflow: hidden;
    background: var(--backdrop);
    font-family: "Open Sans", Arial, sans-serif;
  }
  .stage {
    position: relative; width: 1200px; height: 900px;
    display: flex; justify-content: center; align-items: center; gap: 40px;
  }
  .card {
    position: relative; width: 340px; height: 590px;
    border-radius: 20px; overflow: hidden;
    background: var(--card-black);
    box-shadow: 0 14px 30px rgba(0,0,0,0.45);
  }
  .brand {
    position: absolute; left: 0; right: 0;
    display: flex; justify-content: center; align-items: center; gap: 10px;
  }
  .brand-dot {
    width: 14px; height: 14px; border-radius: 50%;
    background: var(--brand-red);
  }
  .brand-name {
    color: var(--brand-red); font-weight: 700; font-size: 30px;
    letter-spacing: 0.5px; white-space: nowrap;
  }
  .card-front .brand { top: 140px; }
  .card-back .brand { top: 270px; }

  .details {
    position: absolute; left: 0; right: 0; top: 270px; height: 260px;
    background: var(--panel-grey);
    text-align: center; color: var(--text-dark);
  }
  .notch {
    position: absolute; top: 0; left: 50%; transform: translateX(-50%);
    width: 0; height: 0;
    border-left: 13px solid transparent; border-right: 13px solid transparent;
    border-top: 13px solid var(--card-black);
  }
  .person-name { margin-top: 42px; font-size: 24px; font-weight: 700; letter-spacing: 0.3px; }
  .person-title { font-size: 16px; font-weight: 600; margin-top: 2px; }
  .divider { display: block; margin: 10px auto 12px; }
  .contact { font-size: 16px; font-weight: 600; line-height: 21px; }

  .sound-wave {
    position: absolute; left: 50%; bottom: 14px; transform: translateX(-50%);
  }
</style>
</head>
<body>
  <main class="stage">
    <section class="card card-front" aria-label="Card front">
      <div class="brand">
        <span class="brand-dot"></span>
        <span class="brand-name">Lantern Forge</span>
      </div>
      <div class="details">
        <span class="notch"></span>
        <p class="person-name">YOUR NAME</p>
        <p class="person-title">Title</p>
        <svg class="divider" width="230" height="24" viewBox="0 0 230 24" aria-hidden="true">
          <line x1="5" y1="21" x2="225" y2="3" stroke="var(--rule)" stroke-width="2" stroke-linecap="round"/>
        </svg>
        <p class="contact">O: (03) 5550 1234</p>
        <p class="contact">info@lanternforge.com</p>
        <p class="contact">www.lanternforge.com</p>
      </div>
      <svg class="sound-wave" width="220" height="32" viewBox="0 0 220 32" aria-hidden="true">
        <g stroke="var(--wave-grey)" stroke-width="3" stroke-linecap="round">
          <line x1="10" y1="14" x2="10" y2="18"/>
          <line x1="22" y1="11" x2="22" y2="21"/>
          <line x1="34" y1="8" x2="34" y2="24"/>
          <line x1="46" y1="12" x2="46" y2="20"/>
          <line x1="58" y1="5" x2="58" y2="27"/>
          <line x1="70" y1="9" x2="70" y2="23"/>
          <line x1="82" y1="3" x2="82" y2="29"/>
          <line x1="94" y1="10" x2="94" y2="22"/>
          <line x1="106" y1="6" x2="106" y2="26"/>
        </g>
        <g stroke="var(--brand-red)" stroke-width="3" stroke-linecap="round">
          <line x1="118" y1="2" x2="118" y2="30"/>
        </g>
        <g stroke="var(--wave-grey)" stroke-width="3" stroke-linecap="round">
          <line x1="130" y1="7" x2="130" y2="25"/>
          <line x1="142" y1="11" x2="142" y2="21"/>
          <line x1="154" y1="4" x2="154" y2="28"/>
          <line x1="166" y1="10" x2="166" y2="22"/>
          <line x1="178" y1="7" x2="178" y2="25"/>
          <line x1="190" y1="12" x2="190" y2="20"/>
          <line x1="202" y1="10" x2="202" y2="22"/>
          <line x1="214" y1="14" x2="214" y2="18"/>
        </g>
      </svg>
    </section>

    <section class="card card-back" aria-label="Card back">
      <div class="brand">
        <span class="brand-dot"></span>
        <span class="brand-name">Lantern Forge</span>
      </div>
    </section>
  </main>
</body>
</html>
```